KBW needs a professional PP

We are looking for a more professional powerpoint presentation that will be presented to prospective clients. This powerpoint needs to summarize all the services and value that The Harrow Collective has to offer, pretty much giving an overview of the company.

The clients we deal with are Funeral Homes and Funeral Directors, we are an organization dedicated to assisting funeral homes in implementing highly profitable insurance programs while providing the training, support and service along the way. More information is provided in the brochure attached.

We are going for a professional simple theme, we want to get the message across without overwhelming the client.

I have attached our current powerpoint presentation as reference and more information about the our company and what we offer. This one is obviously what we are looking to replace, but the information will be generally the same. It needs to be more visually appealing and convey professionalism.

```html
<!DOCTYPE html>
<html lang="en">
<head>
<meta charset="utf-8">
<title>Company Overview Slides</title>
<link href="https://fonts.googleapis.com/css2?family=Caladea:wght@400;700&family=Yanone+Kaffeesatz:wght@300;400&display=swap" rel="stylesheet">
<style>
  :root{
    --stage:#000;
    --navy:#1f3f7a;
    --blue:#2e6db4;
    --title:#2b4c8c;
    --ink:#1b1b1b;
    --slide-top:#f4f4f4;
    --slide-bottom:#dedede;
    --footer:#f2f2f2;
    --muted:#8a8a8a;
  }
  *{box-sizing:border-box;margin:0;padding:0}
  html,body{width:1200px;height:906px;overflow:hidden;background:var(--stage)}
  body{position:relative;font-family:"Caladea",Georgia,serif;color:var(--ink)}

  .slide{position:absolute;width:555px;height:416px;overflow:hidden;
    background:linear-gradient(180deg,var(--slide-top) 0%,#e9e9e9 55%,var(--slide-bottom) 100%)}
  .slide__rule{position:absolute;top:0;left:0;right:0;height:6px;
    background:linear-gradient(90deg,var(--navy) 0 22%,var(--blue) 22% 40%,#d8dbe2 40% 100%)}
  .slide__title{position:absolute;left:20px;top:26px;font-size:28px;font-weight:400;font-variant:small-caps;
    color:var(--title);letter-spacing:.5px;text-shadow:1px 1px 2px rgba(0,0,0,.25)}
  .slide__footer{position:absolute;left:0;right:0;bottom:0;height:38px;background:var(--footer);
    border-top:1px solid #e4e4e4}
  .wordmark{position:absolute;left:22px;top:12px;font-size:12px;color:var(--title);
    font-variant:small-caps;letter-spacing:.4px;border-bottom:1px solid var(--title)}
  .page-no{position:absolute;right:28px;top:12px;font-size:9px;color:var(--muted)}

  .bullets{position:absolute;left:36px;right:40px;list-style:none}
  .bullets li{position:relative;padding-left:18px;font-size:18px;line-height:21px;margin-bottom:3px}
  .bullets li::before{content:"";position:absolute;left:0;top:7px;border-left:8px solid var(--blue);
    border-top:4px solid transparent;border-bottom:4px solid transparent}
  .bullets .sub{list-style:none;margin:2px 0 3px 4px}
  .bullets .sub li{font-size:14px;line-height:20px;padding-left:20px;margin:0}
  .bullets .sub li::before{content:"–";border:0;top:0;left:0;color:var(--ink)}

  .banner{position:absolute;left:20px;width:463px;height:24px;background:var(--blue);
    color:#fff;font-size:17px;font-variant:small-caps;padding:1px 10px}
  .banner::after{content:"";position:absolute;left:22px;bottom:-8px;border-top:8px solid var(--blue);
    border-left:8px solid transparent;border-right:8px solid transparent}

  .contact__band{position:absolute;left:0;right:0;top:118px;height:178px;background:#f7f7f7;
    box-shadow:0 2px 8px rgba(0,0,0,.25)}
  .contact__bar{position:absolute;left:92px;width:375px;height:9px;background:var(--navy)}
  .contact__name{position:absolute;left:0;right:0;top:28px;text-align:center;font-size:38px;
    color:var(--title);font-variant:small-caps}
  .contact__lines{position:absolute;left:0;right:0;top:92px;text-align:center;font-size:13px;line-height:17px}
  .slide__title--center{left:0;right:0;text-align:center;top:30px}

  .caption{position:absolute;left:620px;top:562px;width:570px;color:#fff;
    font-family:"Yanone Kaffeesatz","Arial Narrow",sans-serif;font-weight:400;font-size:33px;line-height:42px}

  .mini{position:absolute;width:555px;height:414px;transform-origin:0 0;transform:scale(.489)}
  .compare__col{position:absolute;top:112px;width:215px}
  .compare__head{position:relative;height:26px;background:var(--blue);color:#fff;text-align:center;
    font-size:16px;font-variant:small-caps;padding-top:3px}
  .compare__head::after{content:"";position:absolute;left:50%;margin-left:-8px;bottom:-8px;
    border-top:8px solid var(--blue);border-left:8px solid transparent;border-right:8px solid transparent}
  .compare__box{background:#f7f7f7;box-shadow:0 2px 6px rgba(0,0,0,.3);padding:18px 10px 14px 14px;margin-top:2px}
  .compare__box li{font-size:12.5px;line-height:16px;list-style:none;padding-left:10px;position:relative}
  .compare__box li::before{content:"";position:absolute;left:0;top:6px;width:4px;height:4px;background:var(--blue)}
  .process__lead{position:absolute;left:34px;top:86px;font-size:16px}
  .process__band{position:absolute;left:10px;right:10px;top:132px;height:120px;background:#f7f7f7;
    box-shadow:0 2px 6px rgba(0,0,0,.3)}
</style>
</head>
<body>

<section class="slide" style="left:25px;top:23px">
  <div class="slide__rule"></div>
  <h2 class="slide__title">Advanced Wealth Transfer</h2>
  <ul class="bullets" style="top:80px">
    <li>Free Support on Assisting Customers with Advanced Wealth Transfer</li>
    <li>Offer Your Customers Options to Establish:
      <ul class="sub"><li>Trusts</li><li>Annuities</li><li>Wealth Management Options</li></ul></li>
    <li>Assist Customers
      <ul class="sub"><li>Avoid Probate</li><li>Avoid Taxes</li></ul></li>
    <li>Serve Clients on a Personal Level, Leading to Higher Client Satisfaction</li>
    <li>High Commissions (%)</li>
  </ul>
  <footer class="slide__footer"><span class="wordmark">The Harrow Collective</span><span class="page-no">16</span></footer>
</section>

<section class="slide" style="left:617px;top:23px">
  <div class="slide__rule"></div>
  <h2 class="slide__title">Next Steps</h2>
  <div class="banner" style="top:80px">Today</div>
  <ul class="bullets" style="top:122px;left:48px"><li>Contracting with our carriers (10 minutes)</li></ul>
  <div class="banner" style="top:174px">Next appointment</div>
  <ul class="bullets" style="top:216px;left:48px">
    <li>Welcome packet information (10 minutes)</li>
    <li>Training (20 minutes)</li>
  </ul>
  <footer class="slide__footer"><span class="wordmark">The Harrow Collective</span><span class="page-no">18</span></footer>
</section>

<section class="slide" style="left:25px;top:462px">
  <h2 class="slide__title slide__title--center">Contact Information</h2>
  <div class="contact__bar" style="top:109px"></div>
  <div class="contact__band">
    <div class="contact__name">The Harrow Collective</div>
    <div class="contact__lines">Name Here<br>Email@TheHarrowCollective.com<br>555-555-5555<br>www.theharrowcollective.com</div>
  </div>
  <div class="contact__bar" style="top:296px"></div>
</section>

<p class="caption">Plus additional slides if they are required for other presentations down the track...</p>

<section class="slide mini" style="left:617px;top:658px">
  <div class="slide__rule"></div>
  <h2 class="slide__title">Pre Need vs. Final Expense</h2>
  <div class="compare__col" style="left:40px">
    <div class="compare__head">Pre Need</div>
    <ul class="compare__box">
      <li>Simple application</li><li>Higher premiums</li><li>Limited inflation fighters</li><li>Limited range of policy terms</li>
      <li style="visibility:hidden">.</li><li style="visibility:hidden">.</li>
    </ul>
  </div>
  <div class="compare__col" style="left:297px">
    <div class="compare__head">Final Expense</div>
    <ul class="compare__box">
      <li>Simple application</li><li>Lower premiums</li><li>Stronger inflation fighters</li><li>Flexible policy terms</li>
      <li>Broader range of memorial product selections</li><li>Decrease policy lapse due to non-payment</li>
      <li>Larger target market (lower income)</li>
    </ul>
  </div>
  <footer class="slide__footer"><span class="wordmark">The Harrow Collective</span><span class="page-no">6</span></footer>
</section>

<section class="slide mini" style="left:899px;top:658px">
  <div class="slide__rule"></div>
  <h2 class="slide__title">The Process</h2>
  <p class="process__lead">Full service, support, and consultation at no cost to you.</p>
  <div class="process__band">
    <svg width="535" height="120" viewBox="0 0 535 120" font-family="Caladea, serif" font-size="11" text-anchor="middle">
      <g fill="#fff" stroke="#2e6db4" stroke-width="3">
        <polygon points="30,28 140,28 160,60 140,92 30,92 50,60"/>
        <polygon points="150,28 260,28 280,60 260,92 150,92 170,60"/>
        <polygon points="270,28 380,28 400,60 380,92 270,92 290,60"/>
        <polygon points="390,28 480,28 500,60 480,92 390,92 410,60"/>
      </g>
      <g fill="#1b1b1b">
        <text x="97" y="57">Obtain Life</text><text x="97" y="70">Insurance License</text>
        <text x="217" y="46">Receive training</text><text x="217" y="58">on products,</text><text x="217" y="70">services, and</text><text x="217" y="82">sales systems</text>
        <text x="337" y="46">Revive lapsed</text><text x="337" y="58">policies and</text><text x="337" y="70">begin writing</text><text x="337" y="82">new policies</text>
        <text x="447" y="64">Profit</text>
      </g>
    </svg>
  </div>
  <footer class="slide__footer"><span class="wordmark">The Harrow Collective</span><span class="page-no">17</span></footer>
</section>

</body>
</html>
```